Brivanta sales folder inserts

We need the same design for 4 separate service offerings to put inside our sales folder. Each insert should be laid out the same with different images and text and the 2nd, 3rd, and 4th should each be 3/4" shorter than the previous one so that when all 4 are inserted into the folder you see the black strip with text showing what the service offering is. Basically staggered inserts.

Industry/Entity Type

Information Technology

Font styles to use
Sans Serif

Colors
acd136

Requirements
Must have
• Brivanta logo and included text. Keep with the green Pantone 90 and black color scheme
Nice to have
• a better layout and pics

```html
<!DOCTYPE html>
<html lang="en">
<head>
<meta charset="utf-8">
<title>Brivanta CORE-IT — A True IT Partnership</title>
<link rel="stylesheet" href="https://fonts.googleapis.com/css2?family=Oswald:wght@500&family=Roboto+Condensed:ital,wght@0,400;0,700;1,700&family=Roboto:wght@900&display=swap">
<style>
  :root {
    --green: #acd136;
    --green-deep: #9dc03a;
    --black: #000000;
    --ink: #1a1a1a;
    --white: #ffffff;
    --sky-1: #3a6f8e;
    --sky-2: #a9c3d1;
    --sky-3: #dfe9ee;
  }
  * { box-sizing: border-box; margin: 0; padding: 0; }
  html, body { width: 927px; height: 1200px; overflow: hidden; background: var(--white); }
  .insert {
    position: relative; width: 927px; height: 1200px; overflow: hidden;
    font-family: "Roboto Condensed", sans-serif; color: var(--ink);
  }
  .brand {
    position: absolute; left: 58px; top: 40px; display: flex; align-items: center; gap: 14px;
  }
  .brand-mark { width: 40px; height: 40px; background: var(--green); }
  .brand-name {
    font-family: "Roboto Condensed", sans-serif; font-weight: 700; font-size: 40px;
    letter-spacing: 1px; color: var(--black);
  }
  .offer-tab { position: absolute; right: 0; top: 0; width: 345px; height: 113px; }
  .offer-name {
    position: absolute; left: 630px; top: 40px; width: 170px; text-align: center;
    font-family: "Oswald", sans-serif; font-weight: 500; font-size: 42px; line-height: 1;
    color: var(--black); letter-spacing: 1px;
  }
  .hero {
    position: absolute; left: 0; top: 116px; width: 927px; height: 392px;
    background: linear-gradient(100deg, var(--sky-1) 0%, var(--sky-2) 35%, var(--sky-3) 55%, var(--sky-2) 75%, var(--sky-1) 100%);
  }
  .hero-subject {
    position: absolute; left: 420px; top: 40px; width: 300px; height: 350px;
    background: radial-gradient(ellipse at 55% 55%, rgba(40,40,45,.55), rgba(220,220,220,.25) 60%, transparent 75%);
  }
  .hero-wave { position: absolute; left: 0; top: 290px; width: 927px; height: 110px; }
  .hero-title {
    position: absolute; left: 55px; top: 140px;
    font-family: "Roboto", sans-serif; font-weight: 900; font-size: 40px; line-height: 48px;
    color: var(--white); -webkit-text-stroke: 2px var(--black); paint-order: stroke fill;
  }
  .side-panel { position: absolute; left: 566px; top: 494px; width: 307px; height: 706px; }
  .intro-icon { position: absolute; left: 45px; top: 543px; }
  .intro-heading {
    position: absolute; left: 138px; top: 544px;
    font-weight: 700; font-style: italic; font-size: 29px; color: var(--green-deep);
  }
  .intro-sub { position: absolute; left: 138px; top: 590px; font-size: 23px; color: var(--ink); }
  .body-copy { position: absolute; font-size: 14.6px; line-height: 18.2px; }
  .copy-lead { left: 55px; top: 652px; width: 480px; }
  .copy-side { left: 293px; top: 760px; width: 246px; text-align: justify; }
  .copy-tail { left: 51px; top: 936px; width: 494px; text-align: justify; }
  .dashboard {
    position: absolute; left: 55px; top: 762px; width: 218px; height: 130px;
    border: 1px solid #9aa6b2; background: linear-gradient(180deg, #f4f6f8, #e4e9ee);
  }
  .pill {
    position: absolute; left: 582px; width: 311px; height: 28px; background: var(--green);
    border-radius: 14px; display: flex; align-items: center; gap: 8px; padding-left: 10px;
    font-weight: 700; font-style: italic; font-size: 16px; color: var(--black);
  }
  .pill::before { content: ""; width: 11px; height: 11px; border-radius: 50%; background: var(--black); }
  .pill-issues { top: 545px; }
  .pill-advantages { top: 779px; }
  .checklist { position: absolute; left: 587px; width: 280px; list-style: none; }
  .checklist li {
    position: relative; padding-left: 22px; font-size: 14.4px; line-height: 15.2px;
    color: var(--white); margin-bottom: 15px;
  }
  .checklist li svg { position: absolute; left: 0; top: 1px; }
  .checklist strong { color: var(--green); font-weight: 700; }
  .list-issues { top: 584px; }
  .list-advantages { top: 817px; }
  .tagline-band {
    position: absolute; left: 0; top: 1114px; width: 927px; height: 57px; background: var(--green);
    display: flex; align-items: center; justify-content: center;
    font-weight: 700; font-style: italic; font-size: 33px; color: var(--white); letter-spacing: .5px;
  }
</style>
</head>
<body>
<div class="insert">
  <div class="brand"><span class="brand-mark"></span><span class="brand-name">Brivanta</span></div>

  <svg class="offer-tab" viewBox="0 0 345 113" aria-hidden="true">
    <path d="M0 0 H345 V113 H45 Q28 113 24 98 Z" fill="var(--green)"/>
  </svg>
  <div class="offer-name">CORE-IT</div>

  <div class="hero">
    <div class="hero-subject" role="img" aria-label="Businessman in a suit steering a computer-mouse car at speed through streams of binary code"></div>
    <svg class="hero-wave" viewBox="0 0 927 110" preserveAspectRatio="none" aria-hidden="true">
      <path d="M0 32 Q180 2 390 26 T927 20" fill="none" stroke="var(--white)" stroke-width="3"/>
    </svg>
    <h1 class="hero-title">A True<br>IT Partnership</h1>
  </div>

  <svg class="side-panel" viewBox="0 0 307 706" aria-hidden="true">
    <path d="M0 12 Q150 -8 307 12 V706 H0 Z" fill="var(--black)"/>
  </svg>

  <svg class="intro-icon" width="84" height="78" viewBox="0 0 84 78" aria-hidden="true">
    <rect x="58" y="2" width="24" height="72" rx="2" fill="#333"/>
    <rect x="61" y="8" width="18" height="3" fill="#777"/>
    <circle cx="70" cy="40" r="3.5" fill="var(--green)"/>
    <rect x="2" y="18" width="62" height="42" rx="3" fill="#222"/>
    <rect x="6" y="22" width="54" height="32" fill="#4aa3df"/>
    <rect x="26" y="60" width="14" height="9" fill="#444"/>
    <rect x="16" y="68" width="34" height="4" rx="2" fill="#333"/>
  </svg>
  <h2 class="intro-heading">Run Anywhere, Protect Anything</h2>
  <p class="intro-sub">An IT partner not provider.</p>

  <p class="body-copy copy-lead">We understand why your critical business services are so important to your daily operations. This is why we spend so much time aligning our technology support with just such business services. Building a program that relies on 24x7x365 network monitoring coupled with an aggressive preventative maintenance component to ensure optimum uptime for your business.</p>

  <div class="dashboard" role="img" aria-label="Screenshot of a network monitoring dashboard listing devices and their status"></div>

  <p class="body-copy copy-side">One of the major challenges in maintaining a computer network is trying to predict what will fail and when. With our CORE-IT solution, we can prevent many network failures from ever happening. By combining regular and comprehensive preventative maintenance and robust real-time monitoring of</p>

  <p class="body-copy copy-tail">your critical network and desktop devices, we ensure the reliability and stability of your IT assets. This solution is so effective, our customers see almost immediate results. A regularly maintained network means fewer failures, yielding higher productivity and savings on support costs for you. At the same time, your exposure to security risks is dramatically lessened, and frustration from unstable IT resources almost vanishes. We allow our customers to focus on their core business functions by taking the worry out of owning a computer network.</p>

  <div class="pill pill-issues">Do these issues plague your business?</div>
  <ul class="checklist list-issues">
    <li><svg width="16" height="14" viewBox="0 0 16 14"><path d="M1 7 L6 12 L15 1" fill="none" stroke="var(--green)" stroke-width="3"/></svg>Network neglected? Is yours perceived as a "necessary evil" and not as integral to improving business performance?</li>
    <li><svg width="16" height="14" viewBox="0 0 16 14"><path d="M1 7 L6 12 L15 1" fill="none" stroke="var(--green)" stroke-width="3"/></svg>Downtime impact? Are IT outages distracting your staff from their core focus, or prohibiting them from working efficiently?</li>
    <li><svg width="16" height="14" viewBox="0 0 16 14"><path d="M1 7 L6 12 L15 1" fill="none" stroke="var(--green)" stroke-width="3"/></svg>Distracted employees? Do your staff rely on other non-IT employees to deal with distracting IT problems?</li>
  </ul>

  <div class="pill pill-advantages">Program Advantages:</div>
  <ul class="checklist list-advantages">
    <li><svg width="16" height="14" viewBox="0 0 16 14"><path d="M1 7 L6 12 L15 1" fill="none" stroke="var(--green)" stroke-width="3"/></svg><strong>Increased productivity:</strong> Continuous insight into your network lets us reduce the business impact of IT failure by shortening the time from network failure to issue resolution.</li>
    <li><svg width="16" height="14" viewBox="0 0 16 14"><path d="M1 7 L6 12 L15 1" fill="none" stroke="var(--green)" stroke-width="3"/></svg><strong>Reduced business impact from IT failures:</strong> Combining preventative maintenance and remote monitoring means we minimize failures that could impact your business. Your network behaves in a stable and reliable manner.</li>
    <li><svg width="16" height="14" viewBox="0 0 16 14"><path d="M1 7 L6 12 L15 1" fill="none" stroke="var(--green)" stroke-width="3"/></svg><strong>Reduced network downtime through proactive maintenance:</strong> Through regular, preventative maintenance activities designed to keep your network operating efficiently, we reduce the number of emergency incidents you encounter.</li>
  </ul>

  <div class="tagline-band">Stop Buying Downtime – Invest in Uptime</div>
</div>
</body>
</html>
```